electrical contractor business card for professional modern company

I need a business card design for an electrical contractors business. I do all kinds of electricical work from new homes, air conditioning, data and communications. I have a logo design i want on it and have a good idea in my head of what i want it to look like. I like simple yet bold and professional looking. All black background is a must

Target Market(s)

Anyone needing electrical work done

Industry/Entity Type

Electrical

Contact Information for Business Card

company name- KMP Electrical and Data
person name-lewis pembury
phone number- 0468 239 517
website-kmpwire-sample.com.au

Font styles to use
Sans Serif

Requirements
Must have
• email
• website
• logo
• name
• phone number
• list of work i do:
• -electrical
• -air-conditioning
• -data/communications
• -cctv/security
• -domestic/commercial/industrial
• -24hr emergency breakdown repair
Nice to have
• i would like the logo on the front side in the centre taking up most of the card with black background.
• on the rear i want the list of work i do with company info i.e. email, website, my name, phone number. rear of card also black background with orange writing to match the orange in the logo

```html
<!DOCTYPE html>
<html lang="en">
<head>
<meta charset="utf-8">
<title>KMP Electrical and Data – Business Card</title>
<link rel="stylesheet" href="https://fonts.googleapis.com/css2?family=Aldrich&display=swap">
<style>
  :root {
    --backdrop: #bdbdbd;
    --card-black: #050505;
    --signal-orange: #e8531a;
    --divider: #c7461a;
  }
  * { box-sizing: border-box; margin: 0; padding: 0; }
  html, body {
    width: 1200px;
    height: 1000px;
    overflow: hidden;
    background: var(--backdrop);
    font-family: "Aldrich", sans-serif;
  }
  .card-set {
    position: relative;
    width: 1200px;
    height: 1000px;
  }
  .card {
    position: absolute;
    left: 215px;
    width: 770px;
    height: 440px;
    background: var(--card-black);
    border-radius: 4px;
    color: var(--signal-orange);
  }
  .card--front { top: 40px; }
  .card--back  { top: 520px; }

  /* Front */
  .brand {
    position: absolute;
    inset: 0;
    display: flex;
    align-items: center;
    justify-content: center;
  }
  .brand__name {
    font-size: 42px;
    letter-spacing: 2px;
    text-transform: uppercase;
    color: var(--signal-orange);
    font-weight: 400;
  }

  /* Back */
  .contact {
    position: absolute;
    top: 62px;
    left: 0;
    right: 0;
    text-align: center;
  }
  .contact__name {
    font-size: 26px;
    margin-bottom: 14px;
  }
  .contact__line {
    font-size: 19px;
    line-height: 30px;
  }
  .services {
    position: absolute;
    top: 268px;
    left: 0;
    right: 0;
    display: flex;
    justify-content: center;
    align-items: stretch;
  }
  .services__list {
    list-style: none;
    font-size: 19px;
    line-height: 30px;
  }
  .services__list--left { text-align: right; width: 330px; }
  .services__list--right { text-align: left; width: 330px; }
  .services__divider {
    width: 40px;
    display: flex;
    justify-content: center;
  }
  .services__divider svg { display: block; }
</style>
</head>
<body>
<main class="card-set">
  <section class="card card--front" aria-label="Card front">
    <div class="brand">
      <span class="brand__name">KMP Electrical and Data</span>
    </div>
  </section>

  <section class="card card--back" aria-label="Card back">
    <div class="contact">
      <p class="contact__name">Lewis Pembury</p>
      <p class="contact__line">p : 0468 239 517</p>
      <p class="contact__line">e : lewis_pembury@kmpwire-sample.com.au</p>
      <p class="contact__line">w : www.kmpwire-sample.com.au</p>
    </div>

    <div class="services">
      <ul class="services__list services__list--left">
        <li>electrical</li>
        <li>air-conditioning</li>
        <li>domestic/commercial/industrial</li>
      </ul>
      <div class="services__divider">
        <svg width="20" height="100" viewBox="0 0 20 100" aria-hidden="true">
          <line x1="10" y1="0" x2="10" y2="100" stroke="var(--divider)" stroke-width="1.5"/>
          <rect x="5" y="10" width="10" height="10" fill="var(--signal-orange)"/>
          <rect x="5" y="40" width="10" height="10" fill="var(--signal-orange)"/>
          <rect x="5" y="70" width="10" height="10" fill="var(--signal-orange)"/>
        </svg>
      </div>
      <ul class="services__list services__list--right">
        <li>cctv/security</li>
        <li>data/communications</li>
        <li>24hr emergency breakdown repair</li>
      </ul>
    </div>
  </section>
</main>
</body>
</html>
```